Voice Over IP Service

Create a 1-2 page brochure for our voice over IP phone system service.

The color pallet should use these colors..
#e23232 red
#636466 Grey
#434445 Dark grey

```html
<!DOCTYPE html>
<html lang="en">
<head>
<meta charset="utf-8">
<title>NorvaLink – Hosted VoIP Brochure</title>
<link href="https://fonts.googleapis.com/css2?family=Montserrat:wght@300;400;600;700;800&family=Saira+Condensed:wght@300&family=Roboto+Condensed:wght@400;500&display=swap" rel="stylesheet">
<style>
:root{
  --red:#e23232;
  --grey:#636466;
  --dark:#434445;
  --backdrop:#6d6c6d;
  --panel:#eeeeee;
  --orange:#f26a35;
  --yellow:#f2ac1b;
  --green:#2e9a55;
  --teal:#1ba3b6;
  --navy:#1d4f73;
  --white:#ffffff;
}
*{margin:0;padding:0;box-sizing:border-box}
html,body{width:1200px;height:873px;overflow:hidden}
body{background:var(--backdrop);position:relative;font-family:'Montserrat',sans-serif;color:var(--dark)}
.page{position:absolute;top:131px;width:471px;height:610px;background:var(--white);overflow:hidden}
.page--front{left:106px}
.page--back{left:623px}
.brand{position:absolute;top:15px;right:33px;display:flex;align-items:center;gap:4px;font-family:'Montserrat',sans-serif;font-weight:700;font-size:13px;color:var(--red);letter-spacing:-.3px}
.brand__mark{width:9px;height:9px;border:1.6px solid var(--red);border-radius:1px}

.hero-photo{position:absolute;top:44px;left:0;width:471px;height:230px;background:linear-gradient(100deg,#ffffff 0%,#f4f7fa 30%,#dbe5ee 55%,#c9d6e2 75%,#eef2f5 100%)}
.headline{position:absolute;top:150px;left:43px;font-family:'Saira Condensed',sans-serif;font-weight:300;font-size:36px;line-height:37px;letter-spacing:-1.2px;color:var(--red)}
.band{position:absolute;top:274px;left:0;width:471px;height:79px;background:var(--red);padding:14px 0 0 43px;color:var(--white);font-weight:800;font-size:19.5px;line-height:26px}
.dark-section{position:absolute;top:353px;left:0;width:471px;height:224px;background:#4a4a4c}
.city-photo{position:absolute;left:0;top:0;width:230px;height:224px;background:linear-gradient(180deg,rgba(74,74,76,0) 0%,rgba(110,90,70,.55) 55%,#6b5236 100%),linear-gradient(90deg,#5a4a3c 0%,#4a4a4c 100%)}
.col{position:absolute;color:var(--white)}
.col h3{font-weight:800;font-size:11px;line-height:15px;margin-bottom:1px}
.col p{font-weight:300;font-size:8.3px;line-height:11.7px;color:#ededed}
.col--what{left:43px;top:15px;width:180px}
.col--hosted{left:242px;top:15px;width:186px}
.col--why{left:242px;top:118px;width:186px}
.footer{position:absolute;bottom:0;left:0;width:471px;height:33px;display:flex;align-items:center;justify-content:space-between;padding:0 34px 0 43px;font-weight:800;font-size:8.8px;color:var(--red)}
.footer__phone{display:flex;align-items:center;gap:6px}
.footer__phone svg{width:11px;height:11px}

.infographic{position:absolute;top:0;left:0;width:471px;height:274px}
.infographic__icons{position:absolute;top:0;left:0}
.benefit-wheel{position:absolute;left:152px;top:96px;width:136px;height:128px;border-radius:50%;background:radial-gradient(circle at 50% 50%,#ffffff 0%,#ffffff 48%,#e8f2f4 62%,#f6e6d2 80%,#ffffff 100%)}
.hub-title{position:absolute;left:186px;top:146px;font-weight:700;text-align:left}
.hub-title__small{font-size:6.5px;color:var(--navy);display:block}
.hub-title__big{font-size:27px;line-height:23px;color:var(--grey);font-weight:800;display:block;margin-left:1px;letter-spacing:-.5px}
.hub-title__tag{font-size:6.5px;color:var(--red);display:block;text-align:right;margin-top:-1px}
.benefit{position:absolute;font-family:'Roboto Condensed',sans-serif}
.benefit h4{font-weight:500;font-size:9px;line-height:12px;margin-bottom:1px}
.benefit p{font-size:6.5px;line-height:8.4px;color:var(--dark)}
.benefit--mobility{left:224px;top:45px;width:90px}
.benefit--mobility h4{color:var(--yellow)}
.benefit--routing{left:47px;top:108px;width:86px}
.benefit--routing h4{color:var(--orange)}
.benefit--smb{left:314px;top:109px;width:114px}
.benefit--smb h4{color:var(--green)}
.benefit--maint{left:75px;top:228px;width:142px}
.benefit--maint h4{color:var(--navy)}
.benefit--reach{left:282px;top:228px;width:126px}
.benefit--reach h4{color:var(--teal)}

.panel{position:absolute;top:274px;left:0;width:471px;height:271px;background:var(--panel);font-size:8.5px;line-height:11.1px;color:var(--dark)}
.panel__col{position:absolute;top:13px}
.panel__col--left{left:43px;width:186px}
.panel__col--right{left:242px;width:186px}
.panel__intro{font-weight:700;margin-bottom:6px}
.bullets{list-style:none}
.bullets li{position:relative;padding-left:13px;margin-bottom:6px}
.bullets li::before{content:"";position:absolute;left:0;top:4px;width:3.5px;height:3.5px;border-radius:50%;background:var(--dark)}
.bullets b{font-weight:700}
.services-intro{margin-top:10px}
.ticks{list-style:none;margin-top:1px}
.ticks li{position:relative;padding-left:13px;line-height:13px}
.ticks li::before{content:"✓";position:absolute;left:0;font-size:6.5px}
.cta{position:absolute;top:545px;left:0;width:471px;height:32px;background:var(--red);color:var(--white);font-size:9px;line-height:10.3px;text-align:center;padding-top:6px}
.cta b{font-weight:700}
</style>
</head>
<body>

<section class="page page--front">
  <div class="brand"><span class="brand__mark"></span>NorvaLink</div>
  <div class="hero-photo" role="img" aria-label="Smiling call-centre agents wearing headsets in a bright office"></div>
  <h1 class="headline">Is it time<br>for a better<br>phone system?</h1>
  <div class="band">Americas most popular<br>phone system -Voice Over IP (VOIP)</div>
  <div class="dark-section">
    <div class="city-photo" role="img" aria-label="City skyline at dusk blended with a hand holding a phone"></div>
    <div class="col col--what">
      <h3>What is VOIP?</h3>
      <p>VOIP offers a very versatile, low-cost solution for phones and communication that can easily scale with the growth of your business.</p>
    </div>
    <div class="col col--hosted">
      <h3>Hosted VoIP Phone System</h3>
      <p>A fully featured phone system that runs in the cloud with an easy-access online portal for administration and user management. VOIP includes routing work-flows, music on hold, call queues, web phone app and much more.</p>
    </div>
    <div class="col col--why">
      <h3>Why Choose Our Hosted VOIP Phone Service?</h3>
      <p>At NorvaLink our business phone service is best-of-breed that utilizes redundant servers in geographically disperse regions throughout the country to ensure high reliability and sound quality.</p>
    </div>
  </div>
  <footer class="footer">
    <span class="footer__phone"><svg viewBox="0 0 12 12"><circle cx="6" cy="6" r="6" fill="#e23232"/><path d="M4 3.2l1 1.4-.6.7c.4.9 1.1 1.6 2 2l.7-.6 1.4 1-.6 1.1C5.6 8.7 3.3 6.4 3 4z" fill="#fff"/></svg>555-010-4477</span>
    <span>www.norvalink.example</span>
  </footer>
</section>

<section class="page page--back">
  <div class="brand"><span class="brand__mark"></span>NorvaLink</div>
  <div class="infographic">
    <div class="benefit-wheel" role="img" aria-label="Circular diagram of coloured arcs linking the five VoIP benefits"></div>
    <svg class="infographic__icons" width="471" height="274" viewBox="0 0 471 274" fill="none" stroke-linecap="round">
      <rect x="200" y="47" width="14" height="26" rx="2" stroke="#f2ac1b" stroke-width="1.6"/>
      <circle cx="207" cy="69" r="1" fill="#f2ac1b"/>
      <g stroke="#f26a35" stroke-width="1.6">
        <circle cx="92" cy="90" r="6"/>
        <circle cx="92" cy="73" r="2.5"/><circle cx="79" cy="84" r="2.5"/><circle cx="105" cy="84" r="2.5"/><circle cx="81" cy="100" r="2.5"/><circle cx="103" cy="100" r="2.5"/>
        <path d="M92 84V75.5M86.5 87.5L81.5 85M97.5 87.5L102.5 85M87 94L83 98M97 94L101 98"/>
      </g>
      <g fill="#2e9a55">
        <circle cx="349" cy="75" r="4"/><circle cx="361" cy="71" r="4"/><circle cx="373" cy="75" r="4"/>
        <rect x="343" y="81" width="11" height="20" rx="2"/><rect x="355" y="77" width="12" height="24" rx="2"/><rect x="368" y="81" width="11" height="20" rx="2"/>
      </g>
      <g stroke="#1d4f73">
        <circle cx="115" cy="207" r="17" stroke-width="3"/>
        <circle cx="115" cy="207" r="8" stroke-width="4" stroke-dasharray="3 2"/>
        <circle cx="115" cy="207" r="3" stroke-width="2"/>
      </g>
      <path d="M329 184c-4 0-7 3-7 7 0 5 7 12 7 12s7-7 7-12c0-4-3-7-7-7z" fill="#111"/>
      <circle cx="329" cy="191" r="2.5" fill="#fff"/>
    </svg>
    <div class="hub-title">
      <span class="hub-title__small">Benefits of</span>
      <span class="hub-title__big">VoIP</span>
      <span class="hub-title__tag">Telephony</span>
    </div>
    <div class="benefit benefit--mobility"><h4>Mobility</h4><p>VoIP allows for mobility NorvaLink business soft phone is available for dekstop or mobile phone, making your office portable.</p></div>
    <div class="benefit benefit--routing"><h4>Call routing &amp; Automation</h4><p>While we may complain about thede systems at times, think back to before when calls would just go to viocemail, or, even worse, ring perpetually.</p></div>
    <div class="benefit benefit--smb"><h4>Even playing field for SMBs</h4><p>One of the best things about VoIP is that evens the playing field for even the smallest companies. VoIP is scalable and can give a small company just what they need and then grow with them.</p></div>
    <div class="benefit benefit--maint"><h4>Less maintenance</h4><p>Hosted VoIP is managed, at least partially, if not fully, but the service provider. This means no need for maintenance or big IT teams for your company</p></div>
    <div class="benefit benefit--reach"><h4>Even playing field for SMBs</h4><p>VoIP can give you local phone numbers and inexpensive long-distance calling, breaking traditional geographic boundaries.</p></div>
  </div>

  <div class="panel">
    <div class="panel__col panel__col--left">
      <p class="panel__intro">Additionally, people appreciate the following...</p>
      <ul class="bullets">
        <li><b>Competitive pricing:</b> Low flat-fee pricing for unlimited local and long-distance phone service. Our pricing includes an extensive feature list that includes routing by time-frames, easy to create work-flows, company greeting and menu-list (Auto Attendant), ring-all or find the available staff member, call-center reporting and more.</li>
        <li><b>No set-up fees!</b><br>Let us do the heavy-lifting. We will plan and configure your dream phone system as part of our service.</li>
        <li><b>Quality phones</b><br>We include business phones by Vexton and we support most VOIP phone manufacturers including Parrin, Vexton, Calivo, Orbiq and many others.</li>
      </ul>
    </div>
    <div class="panel__col panel__col--right">
      <ul class="bullets">
        <li><b>Call Center</b><br>Track stats on call-center flow, abandoned calls, voicemails, hold times, and more. Our granular reports and call center manager portal allow you to manage your team better than ever.</li>
        <li><b>Audio &amp; Video Conferencing</b><br>Audio conferencing and video conferencing are a rising need for modern business. Remove the need for multiple applications and handle all client communication under one platform.</li>
      </ul>
      <p class="services-intro">We are a full-service VOIP phone system vendor. Our services include...</p>
      <ul class="ticks">
        <li>Planning</li><li>Phone sales</li><li>installation</li><li>support</li><li>management</li>
      </ul>
    </div>
  </div>
  <div class="cta">Call us direct at <b>555-010-4477</b> to get a FREE consultation or demonstration<br>with absolutely no pressure or obligation.</div>
  <footer class="footer">
    <span class="footer__phone"><svg viewBox="0 0 12 12"><circle cx="6" cy="6" r="6" fill="#e23232"/><path d="M4 3.2l1 1.4-.6.7c.4.9 1.1 1.6 2 2l.7-.6 1.4 1-.6 1.1C5.6 8.7 3.3 6.4 3 4z" fill="#fff"/></svg>555-010-4477</span>
    <span>www.norvalink.example</span>
  </footer>
</section>

</body>
</html>
```